Bref créative
Business Cards & Stationary For Law Firm - Use Existing Logo
Harlow Law Offices
I need double sided standard sized Business Card [3.5" x 2"]
I am open to different fonts for the info. I have used Century Gothic before but try any
Professional
Dorian P. Harlow, Esq.
482 N.E. 3rd Avenue
Suite 2206
Coral Vale, Florida 33999
dph@harlowlo.example
www.harlowlo.example
To me the most important thing on a card is that they get your information quickly and easily. I see so many cards that are unmemorable and cluttered with tiny type. I think people want your name and phone easy to read and accessible.
Can put logo and/or any information on either side. Try different designs.

```html
<!DOCTYPE html>
<html lang="en">
<head>
<meta charset="utf-8">
<title>Harlow Law Offices – Business Card</title>
<link rel="stylesheet" href="https://fonts.googleapis.com/css2?family=Marcellus&display=swap">
<style>
  :root {
    --page-bg: #ece9e4;
    --card-white: #ffffff;
    --brand-blue: #2a5cc0;
    --brand-blue-deep: #1d46a3;
    --brand-blue-light: #3a6fd4;
    --ink-blue: #1f4fa6;
    --ink-dark: #1a1a1a;
    --divider: #9aa6bd;
    --on-blue: #ffffff;
  }
  * { box-sizing: border-box; margin: 0; padding: 0; }
  html, body {
    width: 1200px; height: 900px; overflow: hidden;
    background: var(--page-bg);
    font-family: "Marcellus", serif;
  }
  .business-card {
    position: absolute; left: 75px; top: 150px;
    width: 1050px; height: 600px;
    background: var(--card-white);
    box-shadow: 0 10px 30px rgba(0,0,0,0.18);
    overflow: hidden;
  }
  .brand {
    position: absolute; left: 70px; top: 95px;
    display: flex; align-items: center;
  }
  .brand-mark {
    width: 70px; height: 70px;
    background: var(--ink-dark);
  }
  .brand-divider {
    width: 2px; height: 120px; margin: 0 26px 0 30px;
    background: var(--divider);
  }
  .brand-name {
    color: var(--ink-blue);
    font-size: 62px; font-weight: 400; letter-spacing: 3px; line-height: 1;
    text-transform: uppercase;
  }
  .brand-name .brand-sub {
    display: block; font-size: 22px; letter-spacing: 9px; margin-top: 10px;
  }
  .info-band {
    position: absolute; left: 0; top: 240px;
    width: 100%; height: 235px;
    background: linear-gradient(90deg, var(--brand-blue-deep), var(--brand-blue) 45%, var(--brand-blue-light));
  }
  .attorney-name {
    position: absolute; left: 70px; top: 178px;
    color: var(--on-blue); font-size: 27px; letter-spacing: 1px;
    text-transform: uppercase;
  }
  .contact-list {
    position: absolute; left: 660px; top: 18px;
    list-style: none; color: var(--on-blue);
    font-size: 20px; line-height: 1.35; text-transform: uppercase;
  }
  .contact-list li { display: flex; align-items: flex-start; gap: 10px; }
  .contact-list .indent { padding-left: 32px; }
  .contact-icon { width: 22px; height: 22px; flex: none; margin-top: 2px; }
</style>
</head>
<body>
  <main class="business-card">
    <header class="brand">
      <span class="brand-mark" aria-hidden="true"></span>
      <span class="brand-divider" aria-hidden="true"></span>
      <h1 class="brand-name">Harlow<span class="brand-sub">Law Offices</span></h1>
    </header>

    <section class="info-band">
      <p class="attorney-name">Dorian P. Harlow, Esq.</p>
      <ul class="contact-list">
        <li>
          <svg class="contact-icon" viewBox="0 0 22 22" aria-label="Address"><circle cx="11" cy="11" r="11" fill="#fff"/><path d="M11 4.5a4 4 0 0 0-4 4c0 3 4 8 4 8s4-5 4-8a4 4 0 0 0-4-4z" fill="#2a5cc0"/><circle cx="11" cy="8.5" r="1.5" fill="#fff"/></svg>
          <span>482 N.E. 3rd Avenue Suite 2206</span>
        </li>
        <li class="indent">Coral Vale, Florida 33999</li>
        <li>
          <svg class="contact-icon" viewBox="0 0 22 22" aria-label="Phone"><circle cx="11" cy="11" r="11" fill="#fff"/><path d="M7 5.5l2.2-.3 1.2 2.8-1.4 1a7 7 0 0 0 3.8 3.8l1-1.4 2.8 1.2-.3 2.2c-5.2.6-9.9-4.1-9.3-9.3z" fill="#2a5cc0"/></svg>
          <span>786-555-0140</span>
        </li>
        <li>
          <svg class="contact-icon" viewBox="0 0 22 22" aria-label="Fax"><circle cx="11" cy="11" r="11" fill="#fff"/><rect x="6" y="9" width="10" height="6" fill="#2a5cc0"/><rect x="8" y="5.5" width="6" height="4" fill="#2a5cc0"/><rect x="8" y="13" width="6" height="3.5" fill="#fff" stroke="#2a5cc0"/></svg>
          <span>786-555-0147</span>
        </li>
        <li>
          <svg class="contact-icon" viewBox="0 0 22 22" aria-label="Email"><circle cx="11" cy="11" r="11" fill="#fff"/><rect x="5.5" y="7" width="11" height="8" fill="#2a5cc0"/><path d="M5.5 7l5.5 4.5L16.5 7" fill="none" stroke="#fff" stroke-width="1.2"/></svg>
          <span>dph@harlowlo.example</span>
        </li>
        <li>
          <svg class="contact-icon" viewBox="0 0 22 22" aria-label="Website"><circle cx="11" cy="11" r="11" fill="#fff"/><circle cx="11" cy="11" r="5.5" fill="none" stroke="#2a5cc0" stroke-width="1.3"/><ellipse cx="11" cy="11" rx="2.3" ry="5.5" fill="none" stroke="#2a5cc0" stroke-width="1.1"/><path d="M5.5 11h11" stroke="#2a5cc0" stroke-width="1.1"/></svg>
          <span>www.harlowlo.example</span>
        </li>
      </ul>
    </section>
  </main>
</body>
</html>
```